Design for candybags for plimwick.

I need 3 designs for 3 candybags (3 flavors). Or the same design but different colours
- licorice (black)
- sour (green/yellow ish)
- mix (purple from our website #7F1150)
I want our logo to be in the bags (see torvanplimkeda.com) there has to be space in the back of the bag for the bar code and nutritionlist. There has to be a transparent part in the front of the bag, so that you can see the candy in the bag. The size of the bags is 420×594 mm. I want a childish style but at the same time it has to be appealing. I am open minded so if you have a good idea Please let know.

Industry/Entity Type

Food Store

Colors

Designer to choose colors to be used in the design.

Requirements
Must have
• Our logo (www.torvanplimkeda.com)
• Space in the back for the nutritionlist and Bar-Code.
• Transparent part at the front side (or back and front) for the customers to be able to see the candy inside.
• The design artwork format has to be in: PSD, AI or CDR.

```html
<!DOCTYPE html>
<html lang="en">
<head>
<meta charset="utf-8">
<title>Plimwick Candy Bags – Sour</title>
<link rel="stylesheet" href="https://fonts.googleapis.com/css2?family=Caprasimo&family=Archivo+Narrow:wght@400;700&display=swap">
<style>
  :root {
    --bg: #efe6d6;
    --ink: #1c2a17;
    --yellow: #f3e41b;
    --yellow-light: #fbef5a;
    --pink: #e8265f;
    --pink-soft: #f0586f;
    --candy-red: #ef4a4e;
    --candy-green: #9ecf9a;
    --white: #ffffff;
  }
  * { box-sizing: border-box; margin: 0; padding: 0; }
  html, body { width: 1200px; height: 1200px; overflow: hidden; background: var(--bg); }
  .stage { position: relative; width: 1200px; height: 1200px; }
  .bag { position: absolute; top: 282px; width: 454px; height: 672px; }
  .bag--front { left: 132px; }
  .bag--back { left: 620px; }
  .bag svg { position: absolute; inset: 0; width: 100%; height: 100%; }
  .brand-name { font-family: "Caprasimo", serif; fill: var(--yellow); }
  .flavor { font-family: "Caprasimo", serif; fill: var(--ink); text-anchor: middle; }
  .nutrition {
    position: absolute; left: 270px; top: 144px; width: 148px; height: 386px;
    background: var(--white); padding: 5px 6px;
    font-family: "Archivo Narrow", sans-serif; color: #222; font-size: 8px; line-height: 1.4;
  }
  .nutrition__title { font-weight: 700; font-size: 20px; line-height: 1; letter-spacing: -0.3px; border-bottom: 1px solid #222; padding-bottom: 2px; white-space: nowrap; }
  .nutrition__bar { height: 7px; background: #111; margin: 2px 0; }
  .nutrition__row { display: flex; justify-content: space-between; border-bottom: 0.5px solid #999; }
  .nutrition__row--indent { padding-left: 6px; }
  .nutrition__row b { font-weight: 700; }
  .nutrition__note { font-size: 6px; line-height: 1.3; margin: 4px 0; border-bottom: 2px solid #111; padding-bottom: 4px; }
  .nutrition__ingredients { font-size: 8.5px; line-height: 1.75; }
</style>
</head>
<body>
<main class="stage">

  <section class="bag bag--front" aria-label="Front of sour candy bag">
    <svg viewBox="0 0 454 672">
      <defs>
        <radialGradient id="sunFront" cx="50%" cy="62%" r="70%">
          <stop offset="0" stop-color="var(--yellow-light)"/>
          <stop offset="1" stop-color="var(--yellow)"/>
        </radialGradient>
        <linearGradient id="heroFill" x1="0" y1="0" x2="0" y2="1">
          <stop offset="0" stop-color="var(--pink-soft)"/>
          <stop offset="1" stop-color="var(--pink)"/>
        </linearGradient>
      </defs>
      <rect class="bag__body" width="454" height="672" fill="url(#sunFront)"/>
      <path class="bag__band-top" fill="var(--ink)" d="M0 0H454V68C440 100 410 100 398 80C380 62 352 66 344 46C330 34 300 40 290 50C270 44 250 50 240 60C224 48 196 50 186 62C168 58 150 70 140 82C126 64 96 68 88 90C72 112 46 118 30 104C18 118 6 116 0 108Z"/>
      <path class="bag__band-bottom" fill="var(--ink)" d="M0 672H454V590C440 572 410 566 396 580C380 560 350 556 336 578C318 596 296 596 284 580C262 566 238 570 226 586C210 600 180 600 168 584C152 566 124 562 110 580C94 598 66 596 52 576C38 556 14 556 0 570Z"/>
      <g class="logo">
        <circle cx="226" cy="150" r="92" fill="var(--ink)"/>
        <text class="brand-name" x="226" y="146" text-anchor="middle" font-size="22">Torvan</text>
        <text class="brand-name" x="226" y="174" text-anchor="middle" font-size="22">Plimkeda</text>
      </g>
      <text class="flavor" x="226" y="350" font-size="80">SOUR</text>
      <rect role="img" aria-label="Illustration of glossy pink lips over a sour sugar-coated candy lip" x="88" y="380" width="276" height="210" rx="24" fill="url(#heroFill)"/>
    </svg>
  </section>

  <section class="bag bag--back" aria-label="Back of sour candy bag">
    <svg viewBox="0 0 454 672">
      <defs>
        <radialGradient id="sunBack" cx="25%" cy="60%" r="70%">
          <stop offset="0" stop-color="var(--yellow-light)"/>
          <stop offset="1" stop-color="var(--yellow)"/>
        </radialGradient>
        <linearGradient id="windowFill" x1="0" y1="0" x2="1" y2="1">
          <stop offset="0" stop-color="var(--candy-green)"/>
          <stop offset="0.5" stop-color="var(--candy-red)"/>
          <stop offset="1" stop-color="var(--candy-red)"/>
        </linearGradient>
      </defs>
      <rect class="bag__body" width="454" height="672" fill="url(#sunBack)"/>
      <path class="bag__band-top" fill="var(--ink)" d="M0 0H454V60C440 96 412 100 400 80C384 60 360 62 350 46C334 36 306 44 298 56C280 44 262 48 252 60C236 46 206 50 196 64C178 60 160 72 150 84C134 66 108 70 98 92C80 118 50 124 34 108C20 120 6 118 0 110Z"/>
      <path class="bag__band-bottom" fill="var(--ink)" d="M0 672H454V580C438 564 410 562 396 578C380 560 350 556 336 576C318 594 296 594 284 578C262 566 238 568 226 584C210 598 180 598 168 582C152 564 124 560 110 578C94 596 66 594 52 574C38 556 14 556 0 568Z"/>
      <rect class="bag__seam" x="223" y="0" width="28" height="672" fill="var(--ink)"/>
      <g class="logo">
        <circle cx="110" cy="202" r="67" fill="var(--ink)"/>
        <text class="brand-name" x="110" y="198" text-anchor="middle" font-size="16">Torvan</text>
        <text class="brand-name" x="110" y="218" text-anchor="middle" font-size="16">Plimkeda</text>
      </g>
      <text class="flavor" x="112" y="362" font-size="52">SOUR</text>
      <rect role="img" aria-label="Window showing sour sugar-coated candy lips inside" x="42" y="420" width="138" height="108" rx="16" fill="url(#windowFill)"/>
    </svg>

    <div class="nutrition">
      <div class="nutrition__title">Nutrition Facts</div>
      <div>Serving Size 1 fl. oz. (30ml)</div>
      <div>Servings Per Container 1</div>
      <div class="nutrition__bar"></div>
      <div class="nutrition__row"><span>Amount Per Serving</span></div>
      <div class="nutrition__row"><b>Calories 100</b><span>Fat Cal 0</span></div>
      <div class="nutrition__row"><span></span><span>% Daily Value*</span></div>
      <div class="nutrition__row"><span><b>Total Fat</b> 0g</span><span>0%</span></div>
      <div class="nutrition__row nutrition__row--indent"><span>Saturated Fat 0g</span><span>0%</span></div>
      <div class="nutrition__row nutrition__row--indent"><span>Trans Fat 0g</span><span>0%</span></div>
      <div class="nutrition__row"><span><b>Cholesterol</b> 0g</span><span>0%</span></div>
      <div class="nutrition__row"><span><b>Sodium</b> 35mg</span><span>2%</span></div>
      <div class="nutrition__row"><span><b>Potassium</b> 10mg</span><span>0%</span></div>
      <div class="nutrition__row"><span><b>Total Carbohydrate</b> 10g</span><span>4%</span></div>
      <div class="nutrition__row nutrition__row--indent"><span>Dietary Fiber 2g</span><span>8%</span></div>
      <div class="nutrition__row nutrition__row--indent"><span>Sugars 3g</span><span></span></div>
      <div class="nutrition__row"><span><b>Protein</b> 15g</span><span></span></div>
      <div class="nutrition__note">*Percent Daily Values are based on a 2,000 calorie diet. Your daily values may be higher or lower depending on your calorie needs.</div>
      <div class="nutrition__ingredients"><b>Ingredients</b> Sugar, glucose syrup, water, gelatin, tapioca starch, apple pectin, citric acid, malic acid, natural flavors, pear juice concentrate, carnauba wax, colours: red 40, blue 1.</div>
    </div>
  </section>

</main>
</body>
</html>
```